Velvet Orchard Club Members Site

To design a website template that is mobile and desktop friendly for the high net worth members, inner circle club for the rich.
Design of the website must be of luxury feel, a club for the rich.
This website offers redemption of luxury items such as travel packages, and many other items.

Below are the page templates required:

MEMBER SITE

- Login Page
- Dashboard Page (Consists of the member’s redemption points summary, expiry dates)
- Categories Page (The main categories of luxury to redeem)
- Product Page (The actual product details to redeem, showing price, description, title, remarks)
- Redemption Cart (Like a shopping cart which temporary stores the selected items for redemption)
- Checkout Page (Like shopping cart checkout to confirm redemption, fill in address, contact number, name)
- Redemption History (Show a list of items redeemed, with the redemption points used, date)
- Redemption Product Page (Show the redeem product’s details like price, description, title, remarks, date redeemed, points used)
- Inbox (Messaging towards customer service/support)
- Write Message Page
- Read Message Page
- Change Password Page
- My Profile Page

ADMIN SITE

- Login Page
- Dashboard Page (Consists of the whole system redemption points summary in the whole club)
- Redemption Page (To Approve or Cancel Redemptions, or message member to ask more about the redemption)
- Administrator List (List the admins in the system)
- Change Password Page
- Inbox (Messaging towards customer)
- Write Message Page
- Read Message Page
- My Profile Page
- Product Management -> Product List Page, Add/Remove/Edit Product Page
- Category Management -> Category List Page, Add/Remove/Edit Category Page

Note:
All colours should be easily changeable under one css file.
You are feel to use colour tones that reflect high society, rich inner circle club.
The website must be mobile friendly.

Reason: Logo of website uploaded in project brief, pls use the colours tone from the logo. Thanks.

Target Market(s)

High Networth Individuals

Industry/Entity Type

Club

Coding

Coded - Design and coding required

Number of Pages Required

5+ page

Font styles to use
Serif
Sans Serif
Decorative
Script

Requirements
Must have
• It must be desktop and mobile friendly
• All colours should be easily changeable under one css file.

```html
<!DOCTYPE html>
<html lang="en">
<head>
<meta charset="utf-8">
<title>Compose a Message – Velvet Orchard Club</title>
<link rel="stylesheet" href="https://fonts.googleapis.com/css2?family=Open+Sans:wght@400;600;700&display=swap">
<style>
  :root {
    --ink: #333333;
    --ink-soft: #7a7a7a;
    --accent: #2f7fc1;
    --accent-btn: #3a84c7;
    --badge: #1fb8cf;
    --brand-mark: #2aa3b8;
    --line: #c8c8c8;
    --field-border: #c4c4c4;
    --select-arrow-bg: #bdbdc4;
    --editor-bg: #f4f4f4;
    --toolbar-top: #f6f6f6;
    --toolbar-bottom: #e2e2e2;
    --page-bg: #ffffff;
  }
  * { box-sizing: border-box; margin: 0; padding: 0; }
  html, body { width: 1200px; height: 1000px; overflow: hidden; background: var(--page-bg); }
  body { font-family: "Open Sans", Arial, sans-serif; color: var(--ink); }
  .page { position: relative; width: 1200px; height: 1000px; }

  .brand { position: absolute; left: 75px; top: 60px; display: flex; align-items: center; gap: 14px; }
  .brand-square { width: 46px; height: 46px; background: var(--brand-mark); }
  .brand-name { font-size: 26px; font-weight: 700; color: var(--ink); letter-spacing: 1px; text-transform: uppercase; }

  .account { position: absolute; right: 88px; top: 52px; display: flex; align-items: center; gap: 18px; }
  .mail { position: relative; width: 26px; height: 20px; }
  .mail-badge { position: absolute; left: -10px; top: -8px; width: 18px; height: 18px; border-radius: 50%; background: var(--badge); color: #fff; font-size: 11px; font-weight: 600; text-align: center; line-height: 18px; }
  .account-link { font-size: 18px; font-weight: 600; color: var(--ink-soft); text-decoration: none; }

  .main-nav { position: absolute; right: 86px; top: 94px; display: flex; align-items: center; gap: 24px; }
  .main-nav a { font-size: 18px; font-weight: 700; color: var(--ink); text-decoration: none; }

  .page-title { position: absolute; left: 73px; top: 158px; font-size: 24px; font-weight: 600; }
  .title-rule { position: absolute; left: 73px; top: 198px; width: 1042px; border-top: 1px solid var(--line); }
  .breadcrumb { position: absolute; left: 75px; top: 207px; font-size: 15px; font-weight: 600; color: var(--ink-soft); display: flex; align-items: center; gap: 8px; }
  .breadcrumb a { color: var(--accent); text-decoration: none; }
  .crumb-sep { width: 0; height: 0; border-left: 6px solid #888; border-top: 4px solid transparent; border-bottom: 4px solid transparent; }

  .field-label { position: absolute; font-size: 18px; font-weight: 600; color: var(--accent); }
  .select { position: absolute; width: 206px; height: 32px; border: 1px solid var(--field-border); font-size: 16px; font-weight: 600; line-height: 30px; padding-left: 8px; }
  .select-arrow { position: absolute; right: -1px; top: -1px; width: 32px; height: 32px; background: var(--select-arrow-bg); }
  .text-input { position: absolute; left: 74px; top: 357px; width: 734px; height: 32px; border: 1px solid var(--field-border); font-size: 16px; font-weight: 600; line-height: 30px; padding-left: 8px; }

  .editor { position: absolute; left: 75px; top: 435px; width: 1039px; height: 308px; border: 1px solid var(--field-border); }
  .editor-toolbar { height: 47px; background: linear-gradient(var(--toolbar-top), var(--toolbar-bottom)); border-bottom: 1px solid var(--field-border); display: flex; align-items: center; padding-left: 8px; gap: 6px; }
  .tool-group { display: flex; height: 27px; border: 1px solid #b5b5b5; border-radius: 3px; background: linear-gradient(#fbfbfb, #e6e6e6); padding: 0 3px; }
  .tool { width: 28px; display: flex; align-items: center; justify-content: center; font-size: 14px; font-weight: 700; color: #333; font-family: Arial, sans-serif; }
  .editor-body { position: relative; height: 230px; background: var(--editor-bg); padding: 15px 40px 0 20px; font-size: 15px; font-weight: 600; line-height: 21px; }
  .editor-scroll { position: absolute; right: 0; top: 0; width: 16px; height: 100%; background: #ededed; border-left: 1px solid #ddd; }
  .editor-thumb { position: absolute; left: 1px; top: 18px; width: 13px; height: 24px; background: #c1c1c1; }
  .editor-status { height: 29px; background: linear-gradient(#ececec, #d8d8d8); border-top: 1px solid var(--field-border); position: relative; }

  .send-btn { position: absolute; left: 75px; top: 790px; width: 90px; height: 31px; background: var(--accent-btn); color: #fff; border: none; font-family: inherit; font-size: 20px; font-weight: 600; letter-spacing: 0.5px; }

  .footer-rule { position: absolute; left: 74px; top: 877px; width: 1041px; border-top: 1px solid var(--line); }
  .copyright { position: absolute; left: 75px; top: 890px; font-size: 15px; font-weight: 600; color: #999; }
  .footer-nav { position: absolute; right: 86px; top: 887px; display: flex; gap: 21px; }
  .footer-nav a { font-size: 16px; font-weight: 600; color: var(--ink); text-decoration: none; }
</style>
</head>
<body>
<div class="page">
  <header>
    <div class="brand">
      <span class="brand-square"></span>
      <span class="brand-name">Velvet Orchard Club</span>
    </div>
    <div class="account">
      <span class="mail">
        <svg width="26" height="20" viewBox="0 0 26 20"><rect x="1" y="3" width="24" height="15" fill="#9b9b9b"/><path d="M1 3 L13 12 L25 3" fill="none" stroke="#fff" stroke-width="1.5"/><path d="M1 18 L10 10 M25 18 L16 10" stroke="#fff" stroke-width="1.2"/></svg>
        <span class="mail-badge">2</span>
      </span>
      <a class="account-link" href="#">My Account</a>
    </div>
    <nav class="main-nav">
      <a href="#">Home</a>
      <a href="#">Products</a>
      <a href="#">Categories</a>
      <a href="#">About Us</a>
      <svg width="20" height="20" viewBox="0 0 20 20" aria-label="Search"><circle cx="12" cy="8" r="6" fill="none" stroke="#333" stroke-width="2"/><line x1="7.5" y1="12.5" x2="2" y2="18" stroke="#333" stroke-width="2.4" stroke-linecap="round"/></svg>
    </nav>
  </header>

  <main>
    <h1 class="page-title">Compose a Message</h1>
    <div class="title-rule"></div>
    <div class="breadcrumb"><a href="#">Home</a><span class="crumb-sep"></span><span>Compose a Message</span></div>

    <label class="field-label" style="left:74px;top:243px;">Department</label>
    <div class="select" style="left:74px;top:273px;">Sales
      <span class="select-arrow"><svg width="32" height="32" viewBox="0 0 32 32"><path d="M7 9 H25 L16 25 Z" fill="#fff"/></svg></span>
    </div>

    <label class="field-label" style="left:356px;top:243px;">Priority</label>
    <div class="select" style="left:357px;top:273px;">High
      <span class="select-arrow"><svg width="32" height="32" viewBox="0 0 32 32"><path d="M7 9 H25 L16 25 Z" fill="#fff"/></svg></span>
    </div>

    <label class="field-label" style="left:74px;top:328px;">Subject</label>
    <div class="text-input">Problems with purchasing</div>

    <div class="editor">
      <div class="editor-toolbar">
        <div class="tool-group">
          <span class="tool">B</span>
          <span class="tool" style="font-style:italic;font-family:Georgia,serif;">I</span>
          <span class="tool" style="text-decoration:underline;">U</span>
          <span class="tool" style="text-decoration:line-through;">S</span>
        </div>
        <div class="tool-group">
          <span class="tool"><svg width="16" height="10" viewBox="0 0 16 10"><rect x="1" y="2" width="8" height="6" rx="3" fill="none" stroke="#333" stroke-width="1.6"/><rect x="7" y="2" width="8" height="6" rx="3" fill="none" stroke="#333" stroke-width="1.6"/></svg></span>
          <span class="tool"><svg width="16" height="12" viewBox="0 0 16 12"><rect x="1" y="2" width="8" height="6" rx="3" fill="none" stroke="#aaa" stroke-width="1.4"/><path d="M10 7 L15 12 M15 7 L10 12" stroke="#aaa" stroke-width="1.4"/></svg></span>
        </div>
        <div class="tool-group">
          <span class="tool"><svg width="15" height="13" viewBox="0 0 15 13"><rect x="0.8" y="0.8" width="13.4" height="11.4" fill="none" stroke="#333" stroke-width="1.4"/><path d="M2 11 L6 6 L9 9 L11 7 L13 11 Z" fill="#333"/></svg></span>
        </div>
      </div>
      <div class="editor-body">
        <p>Lorem ipsum dolor sit amet, consectetur adipiscing elit. Morbi maximus turpis nec arcu efficitur, in viverra neque scelerisque. Class aptent taciti sociosqu ad litora torquent per conubia nostra.</p>
        <div class="editor-scroll">
          <svg width="14" height="12" viewBox="0 0 14 12" style="position:absolute;top:2px;left:1px"><path d="M4 8 L7 5 L10 8" fill="none" stroke="#444" stroke-width="1.3"/></svg>
          <span class="editor-thumb"></span>
          <svg width="14" height="12" viewBox="0 0 14 12" style="position:absolute;bottom:2px;left:1px"><path d="M4 4 L7 7 L10 4" fill="none" stroke="#444" stroke-width="1.3"/></svg>
        </div>
      </div>
      <div class="editor-status">
        <svg width="10" height="10" viewBox="0 0 10 10" style="position:absolute;right:5px;bottom:6px"><path d="M10 0 V10 H0 Z" fill="#777"/></svg>
      </div>
    </div>

    <button class="send-btn" type="button">SEND</button>
  </main>

  <footer>
    <div class="footer-rule"></div>
    <p class="copyright">© 2016 Velvet Orchard Club. All rights reserved.</p>
    <nav class="footer-nav">
      <a href="#">FAQ</a>
      <a href="#">Legal</a>
      <a href="#">Contact</a>
    </nav>
  </footer>
</div>
</body>
</html>
```